American Painting Company Needs YOU to Design Their Website [Descriptive Brief]

A house painting company based in Knoxville TN, USA needs a fresh, new, fun, and playful--yet, simple, elegant and professional--website made. Here is a link to their existing site:

http://www.brightoakcoatings.example/

We want to keep the same site structure, so the navigation layout will stay the same. However, the video is too small, is too far over in the sidebar, and the overall design is amateur at best. We want something bright, colorful and bold! However, keep in mind the logo in the upper left of the header: The color scheme must include that red, white, and gray.

Here are some examples to look at to get your creative juices flowing!

http://lumenbrushworks.example/

http://www.wfcg.example/

http://www.halvorsen-pike.example/

http://www.tidyframepages.example/painting-company-niche-website/

http://www.quillgridstudio.example/website-templates/painting-company-website-template-83172.html

We have accounts at both pixmeadow.example and snapvault.example. If you use placeholder images from there, that's fine. We can buy the images when and if your design is selected.

Target Market(s)

The audience is the average middle class homeowner. This should appeal to families, couples, and singles who own a home.

Industry/Entity Type

House

Requirements
Must have
• - Lots of color! It's a site about painting homes. People like a variety of colors. Bring out your inner artist, and get bold with your colors!
• - A video place holder. As you can see, there is a video on the existing site, but it's small and hidden. Make it big and put it top left, or in the center.
• -Detailed and organized PSD structure. We're going to turn your design into a website, and to make that work soothly, we ask that you organize you PSD well: name your layers, keep things separated, group and ungroup as necessary, etc.
• A sidebar that goes down the right side of an interior page. We need a homepage, and also one [1] interior page template. We don't need you to make a design for each page. Just the homepage, followed by a simple interior page design that requires only the header/navigation, and a sidebar down the right side.
Should not have
• Coding. This is a design project only.

```html
<!DOCTYPE html>
<html lang="en">
<head>
<meta charset="utf-8">
<title>Brightoak Coatings – About Us</title>
<link href="https://fonts.googleapis.com/css2?family=Oswald:wght@300;400&family=Open+Sans:wght@400;600;700&family=Arimo:wght@400;700&display=swap" rel="stylesheet">
<style>
:root{
  --slate:#3b3f47;
  --slate-dark:#2e3137;
  --red:#b3161c;
  --red-dark:#8a0f14;
  --heading-blue:#2f5496;
  --plaster:#ece8df;
  --text:#333;
  --footer-text:#c9ccd2;
  --orange:#e8743a;
}
*{margin:0;padding:0;box-sizing:border-box}
html,body{width:997px;height:1200px;overflow:hidden}
body{position:relative;background:var(--plaster);font-family:'Open Sans',sans-serif;color:var(--text)}
.top-band{position:absolute;left:0;top:0;width:997px;height:180px;background:var(--slate)}
.plaster{position:absolute;left:0;top:180px;width:997px;height:790px;background:radial-gradient(ellipse at 40% 30%,#f4f1ea,#e3ded3 80%)}
.header{position:absolute;left:38px;top:24px;width:922px;height:108px;background:linear-gradient(90deg,#f3f1ed 0%,#eeebe5 60%,#e47a45 76%,var(--orange) 100%)}
.brand{position:absolute;left:20px;top:38px;display:flex;align-items:center;gap:8px;font-weight:700;font-size:20px;color:var(--red)}
.brand-mark{width:22px;height:22px;background:var(--red)}
.social{position:absolute;right:20px;top:24px;display:flex;gap:6px}
.social span{width:22px;height:22px;border-radius:50%;background:#c4552a}
.phone{position:absolute;right:0;top:56px;height:34px;width:205px;background:#8f9398;color:#fff;font-size:20px;display:flex;align-items:center;padding-left:58px}
.phone-icon{position:absolute;left:-6px;top:-6px;width:46px;height:46px;border-radius:50%;background:#fff;border:4px solid var(--slate)}
.phone-icon svg{position:absolute;left:8px;top:8px}
.nav{position:absolute;left:12px;top:132px;width:974px;height:34px;background:linear-gradient(var(--red),var(--red-dark));display:flex;padding-left:44px}
.nav a{color:#fff;text-decoration:none;font-size:14.5px;line-height:34px;text-transform:uppercase;margin-right:52px}
.hero{position:absolute;left:38px;top:166px;width:922px;height:292px;background:linear-gradient(100deg,#f2efe9 0%,#e9e5dc 45%,#e47a45 62%,#e8743a 100%);box-shadow:0 10px 14px -8px rgba(0,0,0,.45)}
.video{position:absolute;left:30px;top:30px;width:252px;height:218px;background:#fff;overflow:hidden}
.video-title{height:30px;background:#222;color:#fff;font-family:'Arimo',sans-serif;font-size:13px;line-height:30px;padding-left:12px}
.video-frame{position:absolute;left:0;top:30px;width:252px;height:158px;background:linear-gradient(#7a1631 0,#7a1631 45px,#e6e4e0 45px,#cfcac2)}
.play{position:absolute;left:104px;top:94px;width:44px;height:30px;border-radius:7px;background:#222}
.play:after{content:"";position:absolute;left:17px;top:8px;border-left:12px solid #fff;border-top:7px solid transparent;border-bottom:7px solid transparent}
.video-bar{position:absolute;left:0;bottom:0;width:252px;height:30px;background:#3a3a3a;color:#ddd;font-size:11px;line-height:30px;padding-left:110px}
.estimate{position:absolute;left:291px;top:62px;width:631px;height:186px;background:rgba(120,120,125,.55);text-align:center;font-family:'Arimo',sans-serif}
.estimate h2{color:var(--red-dark);font-size:35px;font-weight:400;margin-top:22px;margin-left:-140px}
.estimate p{color:#fff;font-size:17px;font-weight:700;line-height:25px;margin-top:6px;margin-left:-140px;text-shadow:0 1px 2px rgba(0,0,0,.4)}
.breadcrumb{position:absolute;left:58px;top:492px;font-size:14px;color:#555}
h3.section{font-family:'Oswald',sans-serif;font-weight:400;color:var(--heading-blue);font-size:23px;position:absolute}
.thumb{position:absolute;border:3px solid #fff;box-shadow:0 1px 4px rgba(0,0,0,.35)}
.copy{position:absolute;font-size:10.6px;line-height:14.4px;text-align:justify}
.divider{position:absolute;left:58px;top:752px;width:650px;height:1px;background:#d6d1c6}
.quote-mark{position:absolute;left:746px;top:556px;font-family:'Oswald',sans-serif;font-size:52px;color:#9aa0a8;line-height:1}
.testimonial-box{position:absolute;left:780px;top:572px;width:152px}
.testimonial{font-size:9.6px;line-height:13.6px;text-align:justify}
.testimonial-name{display:inline-block;margin-top:10px;font-family:'Arimo',sans-serif;font-size:12px;line-height:14px;border-bottom:1px solid #333}
.footer{position:absolute;left:0;top:970px;width:997px;height:196px;background:var(--slate);color:var(--footer-text)}
.footer h4{position:absolute;font-family:'Oswald',sans-serif;font-weight:300;color:#fff;font-size:20px;line-height:24px}
.quick-links{position:absolute;left:70px;top:46px;list-style:none;font-family:'Arimo',sans-serif;font-size:10.5px;line-height:20px}
.footer-mission{position:absolute;left:240px;top:48px;width:300px;font-family:'Arimo',sans-serif;font-size:9.6px;line-height:11.6px}
.field{position:absolute;height:17px;background:#9ea2a8;border:1px solid #7c8087;color:#eee;font-family:'Arimo',sans-serif;font-size:10px;line-height:15px;padding-left:6px}
.check{position:absolute;left:637px;top:116px;width:16px;height:16px;background:#9ea2a8}
.form-note{position:absolute;left:637px;font-family:'Arimo',sans-serif;font-size:10px;color:#fff;line-height:13px}
.submit{position:absolute;left:641px;top:166px;width:57px;height:18px;background:#6e7fa6;color:#fff;font-family:'Arimo',sans-serif;font-weight:700;font-size:10.5px;text-align:center;line-height:18px}
.bottom-bar{position:absolute;left:0;top:1166px;width:997px;height:34px;background:var(--slate-dark);color:#bbb;font-family:'Arimo',sans-serif;font-size:10.5px;text-align:center;line-height:34px}
</style>
</head>
<body>
<div class="top-band"></div>
<div class="plaster"></div>
<div role="img" aria-label="Paint can spilling red and white paint" style="position:absolute;left:876px;top:700px;width:121px;height:266px;background:linear-gradient(180deg,rgba(236,232,223,0) 0%,#e3ddd1 25%,#b52a24 70%,#8d1f1a 100%)"></div>

<header class="header" role="img" aria-label="Header photo of a white wall with a paint roller and an orange painted section">
  <div class="brand"><span class="brand-mark"></span>Brightoak Coatings</div>
  <div class="social"><span></span><span></span><span></span><span></span></div>
  <div class="phone">
    <span class="phone-icon"><svg width="22" height="22" viewBox="0 0 24 24"><path fill="#e8743a" d="M6.6 10.8a15 15 0 0 0 6.6 6.6l2.2-2.2c.3-.3.7-.4 1-.2 1.1.4 2.3.6 3.6.6.6 0 1 .4 1 1V20c0 .6-.4 1-1 1A17 17 0 0 1 3 4c0-.6.4-1 1-1h3.5c.6 0 1 .4 1 1 0 1.3.2 2.5.6 3.6.1.3 0 .7-.2 1z"/></svg></span>
    (865) 555-0142
  </div>
</header>

<nav class="nav">
  <a>Home</a><a>About Us</a><a>Services</a><a>Gallery</a><a>FAQ</a><a>References</a><a>Contact Us</a>
</nav>

<section class="hero" role="img" aria-label="Painter on a rope seat rolling orange paint onto a wall">
  <div class="video">
    <div class="video-title">Knoxville Painting tips and FREE V</div>
    <div class="video-frame" role="img" aria-label="Video still of the company owner"></div>
    <div class="play"></div>
    <div class="video-bar">0:00 / 0:41</div>
  </div>
  <div class="estimate">
    <h2>Get a FREE ESTIMATE</h2>
    <p>Do you need painting in the greater Knoxville area?<br>Call the Coach today for a FREE painting estimate!<br>licensed and Fully Insured</p>
  </div>
</section>

<div class="breadcrumb">Home&nbsp; ::&nbsp; About Us</div>

<h3 class="section" style="left:56px;top:518px">About Us</h3>
<div class="thumb" role="img" aria-label="Painters on a lift painting a house" style="left:58px;top:565px;width:139px;height:72px;background:linear-gradient(#b9cbe0,#d9c9a6 60%,#d9602a)"></div>
<p class="copy" style="left:204px;top:561px;width:504px">Thanks for visiting Brightoak Coatings online! Please take the time to review our online gallery of examples of work that we have completed as well as our customer testimonials. Please don't miss the opportunity to request Coach Mercer's FREE video painting tips and special report "How to Hire the Right Painter". As a greater Knoxville painting customer please consider contacting Brightoak Coatings by phone and hearing personally why we are the "Painters of Choice" for home and business owners in the greater Knoxville Tennessee area.</p>
<p class="copy" style="left:58px;top:657px;width:650px">When calling Brightoak Coatings customers often want to know about "The Coach". Allow us to share a bit with you about East Tennessee's Painting Coach. Dale "Coach" Mercer, owner of Brightoak Coatings started painting in high school with his high school coach. He continued painting during his college days and then graduated from Ridgeview College in Marlow Ohio. As a local coach he continued painting during the summer as well as during the year. In over 40 years he has painted everything from barn roofs, kitchens, bathrooms, houses, as well as commercial. He has truly "done it all" over the last 40 years.</p>
<div class="divider"></div>

<h3 class="section" style="left:56px;top:778px">Our mission</h3>
<div class="thumb" role="img" aria-label="Painters working on an interior wall" style="left:58px;top:820px;width:136px;height:72px;background:linear-gradient(#d8d6cf,#a9a69c)"></div>
<p class="copy" style="left:204px;top:818px;width:502px">When calling Brightoak Coatings customers often want to know about "The Coach". Allow us to share a bit with you about East Tennessee's Painting Coach. Dale "Coach" Mercer, owner of Brightoak Coatings started painting in high school with his high school coach. He continued painting during his college days and then graduated from Ridgeview College in Marlow Ohio. As a local coach he continued painting during the summer as well as during the year. In over 40 years he has painted everything from barn roofs, kitchens, bathrooms, houses, as well as commercial. He has truly "done it all" over the last 40 years.</p>

<h3 class="section" style="left:746px;top:518px">Testimonials</h3>
<div class="quote-mark">&ldquo;</div>
<div class="testimonial-box">
  <p class="testimonial">We appreciate all your efforts! Thanks for your professionalism, honesty, and integrity. You and your staff are godly men and we will recommend you to all friends and family.</p>
  <span class="testimonial-name">- The Hadleys</span>
</div>

<footer class="footer">
  <h4 style="left:70px;top:14px">Quick Links</h4>
  <ul class="quick-links"><li>Home</li><li>about us</li><li>services</li><li>Gallery</li><li>FAQ</li><li>References</li><li>Contact Us</li></ul>
  <h4 style="left:240px;top:14px">Our Mission</h4>
  <div class="footer-mission">
    <p>Lorem ipsum dolor sit amet, consectetur adipiscing elit. Curabitur in tortor nisl. Curabitur pharetra, ante et semper placerat, mauris tortor ullamcorper libero, quis fringilla tellus nulla eget arcuLorem ipsum dolor sit amet, consectetur adipiscing elit.</p>
    <p style="margin-top:12px">Lorem ipsum dolor sit amet, consectetur adipiscing elit. Curabitur in tortor nisl. Curabitur pharetra, ante et semper placerat, mauris tortor ullamcorper libero, quis fringilla tellus nulla eget arcuLorem ipsum dolor sit amet, consectetur adipiscing elit.</p>
  </div>
  <h4 style="left:635px;top:14px;font-weight:400;font-size:18px">Get 10 Free videos from Dale answering<br>all of your Frequently Asked Questions!</h4>
  <div class="field" style="left:636px;top:68px;width:110px">First Name</div>
  <div class="field" style="left:752px;top:68px;width:110px">Email</div>
  <div class="field" style="left:636px;top:91px;width:110px">Phone</div>
  <div class="check"></div>
  <div class="form-note" style="left:658px;top:119px">Check this box to agree to the SMS terms of service.</div>
  <div class="form-note" style="top:138px">Message &amp; data rates may apply. Reply HELP for help.<br>Reply STOP to cancel.</div>
  <div class="submit">SUBMIT</div>
</footer>
<div class="bottom-bar">© Copyright 2013&nbsp; Brightoak Coatings - All rights reserved.</div>
</body>
</html>
```